Business cards for Remote DBA team

Business cards for team offering database administration, consultation, machine learning and AI services. As of now team is using both
www.fenrowlabs.cz and www.quillbarkgroup.cz URLs

Target Market(s)

IT managers

Industry/Entity Type

It Professional

Contact Information for Business Card

Should include logo
name, email, phone, @fenrowlabs

Font styles to use
Sans Serif

Colors

Designer to choose colors to be used in the design.

```html
<!DOCTYPE html>
<html lang="en">
<head>
<meta charset="utf-8">
<title>Fenrow Labs – Business Cards</title>
<link rel="stylesheet" href="https://fonts.googleapis.com/css2?family=Montserrat:wght@700&family=Open+Sans:wght@400&display=swap">
<style>
  :root {
    --backdrop: #2b2b2d;
    --card: #ffffff;
    --brand-blue: #1b8ac8;
    --ink-grey: #8a8a8a;
    --rule-grey: #9a9a9a;
    --swoosh-grey: #a9a9a9;
    --white: #ffffff;
  }
  * { margin: 0; padding: 0; box-sizing: border-box; }
  html, body {
    width: 1200px; height: 900px; overflow: hidden;
    background: var(--backdrop);
  }
  .canvas { position: relative; width: 1200px; height: 900px; }

  .card {
    position: absolute; left: 270px;
    width: 660px; height: 377px;
    background: var(--card);
    overflow: hidden;
    box-shadow: 0 6px 18px rgba(0,0,0,.35);
  }
  .card--front { top: 45px; }
  .card--back  { top: 478px; }

  /* wordmark */
  .wordmark {
    position: absolute; display: flex; align-items: center; gap: 14px;
  }
  .wordmark__dot {
    width: 22px; height: 22px; border-radius: 50%;
    background: var(--brand-blue);
  }
  .wordmark__name {
    font-family: "Montserrat", sans-serif; font-weight: 700;
    color: var(--brand-blue); font-size: 34px; line-height: 1.05;
    letter-spacing: .5px;
  }
  .card--front .wordmark { left: 60px; top: 140px; }
  .card--back .wordmark { left: 360px; top: 68px; }
  .card--back .wordmark__name { font-size: 30px; }

  .circuit-pattern {
    position: absolute; right: 0; top: 0;
    width: 300px; height: 377px;
    background: linear-gradient(100deg, rgba(27,138,200,0) 0%, rgba(27,138,200,.16) 55%, rgba(27,138,200,.26) 100%);
  }

  /* back card */
  .person { position: absolute; left: 55px; top: 78px; }
  .person__name {
    font-family: "Montserrat", sans-serif; font-weight: 700;
    color: var(--brand-blue); font-size: 24px; letter-spacing: .3px;
  }
  .person__title {
    font-family: "Open Sans", sans-serif; color: var(--ink-grey);
    font-size: 17px;
  }
  .rule {
    position: absolute; left: 48px; top: 158px;
    width: 560px; height: 2px; background: var(--rule-grey);
  }
  .contact {
    position: absolute; list-style: none;
    font-family: "Open Sans", sans-serif; color: var(--ink-grey); font-size: 17px;
  }
  .contact li { display: flex; align-items: center; gap: 12px; line-height: 26px; }
  .contact svg { width: 18px; height: 18px; fill: var(--brand-blue); flex: none; }
  .contact__at {
    width: 18px; flex: none; text-align: center;
    color: var(--brand-blue); font-weight: 400;
  }
  .contact--main { left: 55px; top: 172px; }
  .contact--address { left: 400px; top: 210px; }
  .contact--address li { align-items: flex-start; }
  .contact--address svg { margin-top: 4px; }

  .swoosh { position: absolute; left: 0; bottom: 0; width: 660px; height: 130px; }
  .website {
    position: absolute; right: 50px; bottom: 18px;
    font-family: "Open Sans", sans-serif; color: var(--white); font-size: 18px;
  }
</style>
</head>
<body>
<main class="canvas">

  <section class="card card--front">
    <div class="wordmark">
      <span class="wordmark__dot"></span>
      <span class="wordmark__name">FENROW<br>LABS</span>
    </div>
    <div class="circuit-pattern" role="img" aria-label="Decorative blue circuit-line pattern"></div>
  </section>

  <section class="card card--back">
    <div class="person">
      <p class="person__name">YOUR NAME</p>
      <p class="person__title">Your Title</p>
    </div>

    <div class="wordmark">
      <span class="wordmark__dot"></span>
      <span class="wordmark__name">FENROW<br>LABS</span>
    </div>

    <div class="rule"></div>

    <ul class="contact contact--main">
      <li>
        <svg viewBox="0 0 24 24" aria-hidden="true"><path d="M6.6 10.8a15.1 15.1 0 0 0 6.6 6.6l2.2-2.2a1 1 0 0 1 1-.25 11.4 11.4 0 0 0 3.6.57 1 1 0 0 1 1 1V20a1 1 0 0 1-1 1A17 17 0 0 1 3 4a1 1 0 0 1 1-1h3.5a1 1 0 0 1 1 1c0 1.25.2 2.45.57 3.57a1 1 0 0 1-.25 1z"/></svg>
        123-456-2100
      </li>
      <li>
        <svg viewBox="0 0 24 24" aria-hidden="true"><path d="M2 5h20v14H2z"/><path d="M3 6.5l9 6.5 9-6.5" fill="none" stroke="#fff" stroke-width="1.6"/></svg>
        you@fenrowlabs.cz
      </li>
      <li>
        <span class="contact__at" aria-hidden="true">@</span>
        @fenrowlabs
      </li>
    </ul>

    <ul class="contact contact--address">
      <li>
        <svg viewBox="0 0 24 24" aria-hidden="true"><path d="M12 2a7 7 0 0 0-7 7c0 5 7 13 7 13s7-8 7-13a7 7 0 0 0-7-7zm0 9.5A2.5 2.5 0 1 1 12 6.5a2.5 2.5 0 0 1 0 5z"/></svg>
        <span>Your address, city<br>state, ZIP 0000</span>
      </li>
    </ul>

    <svg class="swoosh" viewBox="0 0 660 130" preserveAspectRatio="none" aria-hidden="true">
      <path d="M0 22 C160 28 330 52 500 84 C330 66 160 54 0 50 Z" fill="var(--swoosh-grey)"/>
      <path d="M0 62 C200 74 420 86 660 68 L660 130 L0 130 Z" fill="var(--brand-blue)"/>
    </svg>
    <p class="website">www.fenrowlabs.cz</p>
  </section>

</main>
</body>
</html>
```